依頼詳細
そこを通れば見落とさずに、入ってこれるような、目立つ看板で、それなりにカッコいいけど親しみやすい雰囲気がいいです。
サイズは縦長で、縦360cm×横90cmです。
記載項目
トーヴリッジ、Tove Ridge、株式会社クオラーク、Quo-Lark
希望イメージ
シンプル 複雑
単色 カラフル
暗い 明るい
日常 高級
遊び心 厳粛
未来的 伝統的
女性的 男性的
希望する色
赤系、緑系、黄・オレンジ系
納品ファイル
• 高解像度JPG (.jpg)
• イラストレーター形式 (.ai)
• フォトショップ形式 (.psd)
補足説明
イメージカラーは明るい緑とオレンジです。
会社のロゴは添付の通りなので、そのQuo-Larkの部分を、Tove Ridge/トーヴリッジにして、その下に「Produced by Quo-Lark Inc」というように入れて使ってもらいたいです。
ロゴを添付します

デザインがわかりやすくてよかった。

たくさんのご提案ありがとうございました。

みなさんの作品がよいので、最後の最後まで悩みました。

また、依頼すると思いますので、宜しくお願い致します。

```html
<!DOCTYPE html>
<html lang="ja">
<head>
<meta charset="utf-8">
<title>Tove Ridge Sign</title>
<link href="https://fonts.googleapis.com/css2?family=Montserrat:wght@600;700&family=Noto+Sans+JP:wght@500&display=swap" rel="stylesheet">
<style>
  :root {
    --page: #ffffff;
    --board: #ffffff;
    --board-edge: #d9d9d9;
    --orange: #f0962a;
    --orange-soft: rgba(240, 150, 42, 0.55);
    --green-soft: rgba(120, 200, 70, 0.45);
    --green: #6cbf3c;
    --charcoal: #3a3a3a;
    --band: #2e1f1c;
  }
  html, body {
    margin: 0;
    width: 778px;
    height: 1200px;
    overflow: hidden;
    background: var(--page);
  }
  .sign {
    position: absolute;
    left: 269px;
    top: 160px;
    width: 240px;
    height: 925px;
    background: var(--board);
    box-shadow: 0 0 0 1px var(--board-edge);
    overflow: hidden;
  }
  .side-band {
    position: absolute;
    left: 205px;
    top: 18px;
    width: 20px;
    bottom: 0;
    background: var(--band);
  }
  .brand-mark {
    position: absolute;
    left: 124px;
    top: 40px;
    width: 64px;
    height: 64px;
    background: var(--orange);
  }
  .accent-field {
    position: absolute;
    left: 12px;
    top: 190px;
    width: 86px;
    height: 460px;
    background: linear-gradient(to right, rgba(255,255,255,0) 0%, var(--green-soft) 45%, var(--orange-soft) 100%);
  }
  .accent-edge {
    position: absolute;
    left: 0;
    top: 0;
    width: 240px;
    height: 6px;
    background: var(--green);
  }
  .brand-name {
    position: absolute;
    left: 116px;
    top: 240px;
    writing-mode: vertical-rl;
    font-family: "Montserrat", sans-serif;
    font-weight: 700;
    font-size: 76px;
    line-height: 1;
    letter-spacing: 1px;
    color: var(--charcoal);
    white-space: nowrap;
  }
  .producer {
    position: absolute;
    left: 100px;
    top: 350px;
    writing-mode: vertical-rl;
    font-family: "Montserrat", sans-serif;
    font-weight: 600;
    font-size: 13px;
    line-height: 1;
    letter-spacing: 1.5px;
    color: var(--charcoal);
    white-space: nowrap;
  }
  .name-kana {
    position: absolute;
    left: 30px;
    top: 672px;
    writing-mode: vertical-rl;
    font-family: "Noto Sans JP", sans-serif;
    font-weight: 500;
    font-size: 35px;
    line-height: 1;
    color: var(--charcoal);
    white-space: nowrap;
  }
</style>
</head>
<body>
  <div class="sign">
    <div class="accent-edge"></div>
    <div class="side-band"></div>
    <div class="brand-mark"></div>
    <div class="accent-field" role="img" aria-label="Soft green and orange accent area behind the brand name"></div>
    <div class="brand-name">Tove Ridge</div>
    <div class="producer">Produced by Quo-Lark Inc</div>
    <div class="name-kana">トーヴリッジ</div>
  </div>
</body>
</html>
```